Piano genealogy graphs template, for a large poster printing

Hello and thank you for your interest in my project.
I need a poster template, so I can create structures similar to the one I have uploaded. I want to completely replace or improve my poor previous design which is attached.
I need to be able to input names and dates into boxes of various colors, arrows pointing between boxes. I would also like to be able to label each graph (not each box).
I am looking at something that would be legible when printed, in a one consistent professional layout of 2A0 (around 1189x1682 mm) poster (I know it is large). The design template required here can include just few sample text boxes with sample flags on a suitable background, for me to multiply later and spread across the whole poster.
The positioning of the boxes is not important.
Please let me know if more clarification is required.
Thank you for your help.

Feel free to follow what I have attached in the file, or change the design completely.

UPDATE 4/12: I have uploaded two more graphs as an example. At this stage of the contest, I would like to have one of those graphs done, and I am planning to offer a 'freelance job' to one or two designers, who will be willing to do the whole 10 graphs on one poster.

Reason: Dear Designers, Since the project is rather complex and large-scale, I have decided to give everyone more time to work on their designs. I will consider extending it further if any of you require additional time. Best wishes, leopold

Dear Designers, I would like to inform you that the contest for my poster is now closed and that I have assigned the prizes. I would like to thank all of you for submiting your high-quality designs, and for your participation. It was a great pleasure working with all of you. Due to the large size of the project itself (large number of graphs to be fitted on a single poster), I had to focus on providing feedback to only those designers who provided projects closest to what I was expecting at the early stages of the contest. I wish you all the best for the future, Kind regards, Leopold

Target Market(s)

Pianists, historians

Industry/Entity Type

Printing

Requirements
Must have
• Consistent design, but allow to clearly delineate various genealogy trees.

```html
<!DOCTYPE html>
<html lang="en">
<head>
<meta charset="utf-8">
<title>Genealogical Trees of Pianists – French Tree</title>
<link href="https://fonts.googleapis.com/css2?family=Cinzel:wght@400;700&family=Crimson+Text:ital,wght@0,400;0,700;1,700&display=swap" rel="stylesheet">
<style>
:root{
  --page:#f1eedb;
  --poster:#e3d184;
  --header:#dccb82;
  --footer:#cfbb6c;
  --ink:#2b2118;
  --line:#3a2a1f;
  --faint:#c9b06a;
  --map:#d6c174;
  --mark:#c4542e;
  --dot:#2a8a3a;
  --keys:#f2ecd6;
}
*{margin:0;padding:0;box-sizing:border-box}
html,body{width:900px;height:1200px;overflow:hidden;background:var(--page)}
body{position:relative;font-family:"Crimson Text",Georgia,serif;color:var(--ink)}
.poster{position:absolute;left:113px;top:10px;width:674px;height:1170px;border:3px solid #fff;background:var(--poster)}
.header{position:absolute;left:0;top:0;width:100%;height:80px;background:var(--header)}
.title{position:absolute;left:0;top:52px;width:100%;text-align:center;font-family:"Cinzel",serif;font-weight:400;font-size:17px;letter-spacing:.5px;color:var(--ink)}
.rule{position:absolute;left:0;width:100%;background:var(--line)}
.keyboard{position:absolute;left:0;top:88px;width:100%;height:78px;background:linear-gradient(#e9e1c6,var(--keys) 40%,#e6dcbc)}
.keyboard-base{position:absolute;left:0;top:166px;width:100%;height:7px;background:#cdb66a}
.tree-label{position:absolute;left:38px;top:212px;font-family:"Cinzel",serif;font-weight:700;color:var(--faint);line-height:1}
.tree-label .big{font-size:56px;display:block}
.tree-label .small{font-size:24px;display:block;margin-left:142px;margin-top:2px}
.map{position:absolute;left:180px;top:300px;width:310px;height:350px;background:var(--map);opacity:.55;border-radius:40% 30% 35% 45%}
.piano-faint{position:absolute;left:455px;top:182px;width:150px;height:118px;background:var(--faint);opacity:.35;border-radius:6px}
.piano-icon{position:absolute;left:315px;top:176px;width:36px;height:30px;background:var(--line);border-radius:12px 12px 3px 3px}
.links{position:absolute;left:0;top:0}
.node{position:absolute;width:240px;text-align:center;font-size:10.5px;line-height:12px}
.node .name{font-weight:700}
.node .dates{font-weight:700}
.node .mark{color:var(--mark);font-size:10px}
.students{list-style:none}
.abroad::before{content:"";display:inline-block;width:5px;height:5px;border-radius:50%;background:var(--dot);margin-right:4px;vertical-align:1px}
.flag{display:inline-block;width:14px;height:9px;margin-left:3px;vertical-align:-1px}
.be{background:linear-gradient(90deg,#111 33%,#f4d01c 33% 66%,#d3242b 66%)}
.us{background:linear-gradient(90deg,#2b3d7c 40%,transparent 40%) top/100% 50% no-repeat,repeating-linear-gradient(#c2202c 0 1.3px,#fff 1.3px 2.6px)}
.bg{background:linear-gradient(#fff 33%,#1e8f4e 33% 66%,#d3242b 66%)}
.au{background:#1f3c8c}
.uk{background:linear-gradient(#c2202c 0 0) center/100% 2px no-repeat,linear-gradient(#c2202c 0 0) center/2px 100% no-repeat,#1f3c8c}
.it{background:linear-gradient(90deg,#1e8f4e 33%,#fff 33% 66%,#d3242b 66%)}
.de{background:linear-gradient(#111 33%,#d3242b 33% 66%,#f4c21c 66%)}
.pl{background:linear-gradient(#fff 50%,#d3242b 50%)}
.ch{background:linear-gradient(#fff 0 0) center/8px 2px no-repeat,linear-gradient(#fff 0 0) center/2px 8px no-repeat,#d3242b}
.ro{background:linear-gradient(90deg,#1f3c8c 33%,#f4d01c 33% 66%,#d3242b 66%)}
.gr{background:repeating-linear-gradient(#2a5fb0 0 1px,#fff 1px 2px)}
.br{background:radial-gradient(circle,#f4d01c 3px,#1e8f4e 3.5px)}
.tr{background:radial-gradient(circle at 40% 50%,#fff 2px,#d3242b 2.5px)}
.ru{background:linear-gradient(#fff 33%,#1f3c8c 33% 66%,#d3242b 66%)}
.footer{position:absolute;left:0;top:1050px;width:100%;height:114px;background:var(--footer)}
.legend{position:absolute;left:34px;top:17px;list-style:none;font-size:10px;line-height:18px;font-style:italic;font-weight:700}
.legend .sym{display:inline-block;width:20px;font-style:normal}
.legend .dot{color:var(--dot)}
.legend .hash{color:var(--mark)}
.caption{position:absolute;left:0;top:84px;width:100%;text-align:center;font-size:10.5px}
</style>
</head>
<body>
<main class="poster">
  <header class="header"><h1 class="title">Genealogical Trees of Pianists</h1></header>
  <div class="rule" style="top:80px;height:2px"></div>
  <div class="rule" style="top:84px;height:2px"></div>
  <div class="keyboard" role="img" aria-label="Row of piano keys across the header"></div>
  <div class="keyboard-base"></div>

  <div class="map" role="img" aria-label="Faint map of France"></div>
  <div class="piano-faint" role="img" aria-label="Faint grand piano"></div>
  <div class="tree-label"><span class="big">French</span><span class="small">Tree</span></div>
  <div class="piano-icon" role="img" aria-label="Grand piano icon"></div>

  <svg class="links" width="674" height="1050" viewBox="0 0 674 1050" fill="none" stroke="#3a2a1f" stroke-width="2">
    <path d="M332 238V268M332 295V323M125 323H539M125 323V350M332 323V350M539 323V350"/>
    <path d="M332 460V485M125 485H539M125 485V512M332 485V512M539 485V512"/>
    <path d="M332 635V663M69 663H565M69 663V690M254 663V744M402 663V690M487 663V808M565 663V690"/>
    <path d="M487 898V925M254 773V863M179 863H334M179 863V892M334 863V892"/>
    <g fill="#3a2a1f" stroke="none">
      <circle cx="332" cy="268" r="3"/><circle cx="332" cy="323" r="3"/><circle cx="332" cy="485" r="3"/><circle cx="332" cy="663" r="3"/><circle cx="487" cy="925" r="3"/><circle cx="254" cy="863" r="3"/>
    </g>
  </svg>

  <div class="node" style="left:212px;top:210px"><p class="name">Laurent-Honoré Vasselin</p><p class="dates">(1775 - 1834)</p></div>
  <div class="node" style="left:212px;top:268px"><p class="name">Pierre Delacombe</p><p class="dates">(1785 - 1853)</p></div>

  <div class="node" style="left:5px;top:352px"><p class="name">Charles-Victor Arnaud</p><p class="dates">(1813-1888)</p></div>
  <div class="node" style="left:212px;top:352px"><p class="name">Antoine-Louis Berthelot</p><p class="dates">(1822-1890)</p><p class="mark">#</p>
    <ul class="students"><li>Claude Feraud (1862-1918)</li><li>Vincent Lebrun (1851-1931)</li><li>Antonin Berthelot (1850-1907)</li><li>Alphonse Carrel (1842-1907)</li><li>Francis Guérin (1839-1934)</li><li>Georges Dubreuil (1838-1875)</li></ul></div>
  <div class="node" style="left:419px;top:352px"><p class="name abroad">César Morand<span class="flag be"></span></p><p class="dates">(1822-1890)</p></div>

  <div class="node" style="left:5px;top:514px"><p class="name">Marguerite Fabre</p><p class="dates">(1862-1918)</p><p class="mark">#</p>
    <ul class="students"><li>Samson Morel (1924-1970)</li><li>Nicole Hervé-Schmitt (1923-2001)</li><li>Annie Delorme (1920-1988)</li><li class="abroad">Earl Whitby (1915-2010)<span class="flag us"></span></li><li>Gaby Castelnau (1901-1999)</li><li>Jacques Ferrand (1900-1979)</li></ul></div>
  <div class="node" style="left:212px;top:514px"><p class="name">Louis Garnier</p><p class="dates">(1843-1919)</p><p class="mark">#</p>
    <ul class="students"><li>Gaby Castelnau (1901-1999)</li><li>Robert Castelnau (1899-1972)</li><li>E. Robert Stoltz (1889-1949)</li><li>Marcel Duret (1886-1971)</li><li class="abroad">Alfredo Cavalli (1883-1947)<span class="flag it"></span></li><li class="abroad">Edouard Reiner (1873-1929)<span class="flag de"></span></li><li class="abroad">Sigismond Sadowski (1870-1946)<span class="flag pl"></span></li></ul></div>
  <div class="node" style="left:419px;top:514px"><p class="name abroad">Olga Varenkova<span class="flag us"></span></p><p class="dates">(1882-1948)</p><p class="mark">#</p>
    <ul class="students"><li class="abroad">Jerome Lindqvist (1932)<span class="flag us"></span></li><li class="abroad">Alexis Wendt (1929)<span class="flag bg"></span></li><li class="abroad">Raymond Lasker (1923-1988)<span class="flag us"></span></li><li class="abroad">Bruce Halford (1922-1953)<span class="flag au"></span></li><li class="abroad">William Kessler (1922-1953)<span class="flag us"></span></li><li>Eugene Lark (1918-1985)</li><li class="abroad">Rosalyn Tarrant (1914-2003)<span class="flag us"></span></li></ul></div>

  <div class="node" style="left:-25px;top:692px"><p class="name abroad">Alfred Corvin<span class="flag ch"></span></p><p class="dates">(1877-1962)</p><p class="mark">#</p>
    <ul class="students"><li class="abroad">Dino Carrara (1941-1974)<span class="flag it"></span></li><li>Eric Heyraud (1936)</li><li class="abroad">Jerome Lindqvist (1932)<span class="flag us"></span></li><li class="abroad">Ruth Sokolska (1925)<span class="flag us"></span></li><li class="abroad">Dinu Lascaris (1917-1950)<span class="flag ro"></span></li><li class="abroad">Gina Bakaris (1910-1976)<span class="flag gr"></span></li><li class="abroad">Vlado Pernik (1904-2002)<span class="flag pl"></span></li><li>Yvonne Lefranc (1898-1986)</li><li class="abroad">Magda Tavares (1893-1986)<span class="flag br"></span></li></ul></div>
  <div class="node" style="left:134px;top:746px"><p class="name">Yves Narbonne</p><p class="dates">(1890-1956)</p></div>
  <div class="node" style="left:282px;top:692px"><p class="name">Jean Dorval</p><p class="dates">(1907-1982)</p><p class="mark">#</p>
    <ul class="students"><li class="abroad">Idil Berker (1941)<span class="flag tr"></span></li><li class="abroad">Arthur Moreno Luz (1940)<span class="flag br"></span></li><li>Dominique Marlin (1938)</li><li>Philippe Estrade (1934)</li></ul></div>
  <div class="node" style="left:445px;top:692px"><p class="name abroad">Lazare Lavigne<span class="flag be"></span></p><p class="dates">(1882-1964)</p><p class="mark">#</p>
    <ul class="students"><li class="abroad">Alexander Uvarov (1910-1972)<span class="flag ru"></span></li><li>Monique Hallé (1909-1987)</li><li class="abroad">Solomon Curtis (1902-1988)<span class="flag uk"></span></li><li class="abroad">Clara Hasdeu (1895-1960)<span class="flag ro"></span></li></ul></div>

  <div class="node" style="left:367px;top:811px"><p class="name">Marcel Ciprani</p><p class="dates">(1891-1980)</p><p class="mark">#</p>
    <ul class="students"><li class="abroad">Jean-Marc Lusardi (1958)<span class="flag tr"></span></li><li>Cécile Oudin (1936)</li><li class="abroad">John Carrick (1930)<span class="flag au"></span></li><li class="abroad">Hephzibah Merrill (1920-1981)<span class="flag us"></span></li></ul></div>
  <div class="node" style="left:367px;top:929px"><p class="name">Yvonne Lorrain</p><p class="dates">(1924-2010)</p><p class="mark">#</p>
    <ul class="students"><li class="abroad">Nicholas Andric (1970)<span class="flag us"></span></li><li>Pierre-Laurent Amiel (1957)</li><li class="abroad">Peter Donnelly (1953)<span class="flag uk"></span></li><li>Michel Bérard (1950)</li><li class="abroad">Paul Crofton (1944)<span class="flag uk"></span></li></ul></div>

  <div class="node" style="left:59px;top:895px"><p class="name">Pierre Sanclair</p><p class="dates">(1916-2008)</p><p class="mark">#</p>
    <ul class="students"><li>Jean-Philippe Colbert (1948)</li><li>Jacques Rouvel (1947)</li><li>Jean-Bernard Pomerol (1944)</li></ul></div>
  <div class="node" style="left:214px;top:895px"><p class="name">Lucette Deschamps</p><p class="dates">(1906)</p><p class="mark">#</p>
    <ul class="students"><li>Jean-Yves Thibault (1961)</li><li>Marielle Lavergne (1952)</li><li>Pascal Rogier (1951)</li><li>Katia Lavergne (1950)</li></ul></div>

  <footer class="footer">
    <ul class="legend">
      <li><span class="sym dot">●</span>Indicates People born in the respective country flag shown. All others were born in France.</li>
      <li><span class="sym hash">#</span>Indicates the students of the above personal.</li>
    </ul>
    <p class="caption">Genealogical Trees of Pianists - French Tree</p>
  </footer>
</main>
</body>
</html>
```